Webdesign für Unternehmen im Bereich der Prozessautomatisierung und Gebäudeautomation
Zielgruppe
Wir befinden uns derzeit in der Gründungsphase und möchten ein neuer Dienstleister im Bereich der Automatisierung werden. Wir haben uns dazu auf zwei Kernaufgaben spezialisiert:
Prozessautomatisierung und Gebäudeautomation.
Aufgabenstellung
Gesucht wird nur eine Seite für Bereich Prozessautomatisierung. Die weiteren Seiten kommen zu eine späteren Zeitpunkt.
Texte sind leider noch nicht vorhanden. Sie können Fülltext verwenden oder sich selbst etwas überlegen.
Für das Design eventuell relevante Punkte sind die folgenden:
Die Seite soll locker gestaltet sein. Die betrachtende Person darf nicht vom Text erschlagen werden.
Ziel mit unserer Applikation:
… Kosten- und Zeitersparnis beim Kunden zu erzielen!
… Fehler zu reduzieren und ganz zu vermeiden!

```html
<!DOCTYPE html>
<html lang="de">
<head>
<meta charset="utf-8">
<title>FLOWGRID – ERP-Applikation</title>
<link rel="stylesheet" href="https://fonts.googleapis.com/css2?family=Work+Sans:wght@400;500;600;700&display=swap">
<style>
:root{
  --blue:#0f6db5;
  --blue-light:#2a8fd6;
  --ink:#2b2b2f;
  --text:#55575c;
  --muted:#8b8d93;
  --footer:#5a6178;
  --footer-dark:#4f5569;
  --footer-text:#c9ccd6;
  --white:#fff;
}
*{box-sizing:border-box;margin:0;padding:0}
html,body{width:1200px;height:2905px;overflow:hidden}
body{position:relative;background:var(--white);font-family:"Work Sans",sans-serif;color:var(--text)}
.abs{position:absolute}
a{color:inherit;text-decoration:none}

/* header */
.brand{left:150px;top:14px;display:flex;align-items:center;gap:10px;font-weight:700;font-size:23px;color:var(--ink);letter-spacing:.5px}
.brand .mark{width:34px;height:34px;background:var(--blue)}
.nav{left:444px;top:21px;width:456px;display:flex;justify-content:space-between;font-size:10.5px;color:var(--text);white-space:nowrap}
.nav .active{color:var(--ink);font-weight:600;position:relative}
.nav .active::after{content:"";position:absolute;left:0;top:19px;width:14px;height:2px;background:var(--blue)}
.btn{display:flex;align-items:center;justify-content:center;color:#fff;font-size:9px;font-weight:500;letter-spacing:.4px;background:linear-gradient(90deg,var(--blue),var(--blue-light));box-shadow:0 3px 8px rgba(15,109,181,.3);border-radius:2px}
.btn-estimate{left:931px;top:12px;width:119px;height:31px}

/* hero */
.hero-title{left:150px;top:164px;width:420px;font-size:28px;font-weight:700;line-height:33px;color:var(--ink);letter-spacing:.6px}
.hero-text{left:149px;top:288px;width:420px;font-size:15px;line-height:25px;letter-spacing:.2px}
.hero-link{left:150px;top:396px;font-size:15px;color:var(--blue);letter-spacing:.2px;white-space:nowrap}
.hero-art{left:580px;top:107px;width:470px;height:446px;border-radius:40% 20% 30% 40%;background:radial-gradient(ellipse at 60% 45%,#c9bfe8 0%,#e0dcf3 40%,#f6f6fa 75%,#fff 100%)}

/* intro */
.center{left:0;width:1200px;text-align:center}
.h2{font-size:21px;font-weight:600;color:var(--ink);letter-spacing:.8px}
.intro-sub{top:628px;font-size:14px;line-height:18px;letter-spacing:.4px}
.finder{top:716px;font-size:15px;letter-spacing:.6px;color:var(--ink)}
.tabs{left:159px;top:772px;width:880px;display:flex;justify-content:space-between;font-size:10.5px;color:var(--muted);letter-spacing:.2px}
.tabs .on{color:var(--ink);font-weight:600}
.photo{left:0;top:798px;width:1200px;height:300px;background:linear-gradient(180deg,#8d99a6 0%,#b9c0c6 45%,#d5d9dd 70%,#c7cbd0 100%)}
.stat{width:94px;height:94px;border-radius:50%;background:#eeeff1;text-align:center;padding-top:27px}
.stat svg{position:absolute;left:0;top:0}
.stat b{display:block;font-size:14px;color:var(--blue);font-weight:600}
.stat span{display:block;font-size:7.5px;line-height:8px;color:var(--text);margin-top:3px}
.device{left:635px;top:934px;width:520px;height:250px}

.why-sub{top:1316px;width:660px;left:270px;font-size:14px;line-height:18px;letter-spacing:.3px}
.btn-anfrage{left:448px;top:1511px;width:118px;height:31px}
.btn-support{left:634px;top:1511px;width:118px;height:31px}

/* success band */
.band{left:0;top:1670px;width:1200px;height:587px;background:linear-gradient(180deg,#0f6db5,#3189c9)}
.band-sub{top:1764px;font-size:14px;line-height:18px;color:#fff;letter-spacing:.4px}
.feat-art{width:170px;height:150px;border-radius:30px;background:radial-gradient(circle at 45% 50%,#bfe9f6 0%,#6fc3e6 45%,rgba(40,120,190,0) 75%)}
.feat-text{width:250px;text-align:center;font-size:11px;line-height:19px;color:#fff;letter-spacing:.2px}
.band-link{top:2162px;font-size:14px;color:#fff;letter-spacing:.6px}

/* trust */
.trust-sub{top:2374px;font-size:14px;letter-spacing:.7px}
.logos{left:150px;top:2448px;width:900px;display:flex;justify-content:space-between;align-items:center;font-size:22px;font-weight:700;color:#1d1d22}
.chat{left:1133px;top:2311px;width:54px;height:54px;border-radius:50%;background:var(--blue)}

/* footer */
.footer{left:0;top:2558px;width:1200px;height:347px;background:var(--footer)}
.footer-bar{left:0;top:2842px;width:1200px;height:63px;background:var(--footer-dark)}
.fcol{top:2606px}
.fcol h4{font-size:11px;font-weight:600;color:#fff;margin-bottom:10px}
.fcol li{list-style:none;font-size:9px;line-height:23.7px;color:var(--footer-text)}
.fcol.bold li{font-size:11px;font-weight:600;color:#fff;line-height:23.7px}
.hiring{font-size:6px;color:#9ecbf0;vertical-align:super}
.fbrand{left:150px;top:2860px;font-size:20px;font-weight:700;color:#fff;display:flex;gap:8px;align-items:center}
.fbrand .mark{width:28px;height:28px;background:#fff}
.lang{left:376px;top:2861px;width:148px;height:27px;border:1px solid #7a8197;background:#636a81;color:#fff;font-size:9px;font-weight:600;display:flex;align-items:center;justify-content:space-between;padding:0 14px}
.legal{left:609px;top:2868px;display:flex;gap:16px;font-size:9.5px;color:var(--footer-text)}
.social{left:935px;top:2867px;display:flex;gap:12px;font-size:9.5px;font-weight:600;color:var(--footer-text)}
</style>
</head>
<body>

<header>
  <div class="abs brand"><span class="mark"></span>FLOWGRID</div>
  <nav class="abs nav">
    <a class="active">ERP-Applikation</a><a>Gebäudeautomation</a><a>Kundennutzen</a><a>Unternehmen</a><a>Kontakt</a>
  </nav>
  <a class="abs btn btn-estimate">GET ESTIMATE</a>
</header>

<section class="hero">
  <h1 class="abs hero-title">Seien Sie das Unternehmen von morgen. Und das schon heute.</h1>
  <p class="abs hero-text">Lorem ipsum dolor sit amet Consetetur sadipscing elitr sed diam nonumy eirmod. Tempor invidunt ut labore et dolore magna aliquyam erat.</p>
  <a class="abs hero-link">Entdecke die ERP-Lösung der nächsten Generation ↓</a>
  <div class="abs hero-art" role="img" aria-label="Isometrische Illustration: Datenwand mit Weltkarte und Diagrammen, zwei Personen auf einer Plattform"></div>
</section>

<section class="apps">
  <h2 class="abs center h2" style="top:589px">KMU mit skalierbarer ERP-Software steuern</h2>
  <p class="abs center intro-sub">Erfassen Sie alle Daten in einem integrierten ERP-System (Enterprise<br>Resource Planning) für kleine und mittlere Unternehmen.</p>
  <p class="abs center finder">FINDEN SIE <b>IHRE APPLIKATION.</b></p>
  <div class="abs tabs"><span class="on">LAGER</span><span>EINKAUF/VERKAUF</span><span>PERSONAL</span><span>ARBEITSZEITERFASSUNG</span><span>DATA-MANAGEMENT</span><span>RECHNUNGSWESEN</span><span>MOBILE LÖSUNGEN</span><span>TICKETSUPPORT</span></div>
  <div class="abs photo" role="img" aria-label="Foto einer Lagerhalle mit Hochregalen"></div>

  <div class="abs stat" style="left:234px;top:1051px">
    <svg width="94" height="94"><circle cx="47" cy="47" r="45" fill="none" stroke="#0f6db5" stroke-width="3.5" stroke-dasharray="175 300" transform="rotate(-90 47 47)"/></svg>
    <b>62%</b><span>höhere<br>Automatisierung</span>
  </div>
  <div class="abs stat" style="left:347px;top:1051px">
    <svg width="94" height="94"><circle cx="47" cy="47" r="45" fill="none" stroke="#0f6db5" stroke-width="3.5" stroke-dasharray="113 300" transform="rotate(-90 47 47)"/></svg>
    <b>40%</b><span>schnellere<br>Durchlaufzeiten</span>
  </div>
  <div class="abs stat" style="left:459px;top:1051px">
    <svg width="94" height="94"><circle cx="47" cy="47" r="45" fill="none" stroke="#0f6db5" stroke-width="3.5" stroke-dasharray="90 300" transform="rotate(-90 47 47)"/></svg>
    <b>32%</b><span>sichtbare<br>Effizienzsteigerung</span>
  </div>

  <svg class="abs device" viewBox="0 0 520 250" role="img" aria-label="Videoplayer">
    <rect x="70" y="0" width="380" height="226" rx="8" fill="#d9dadc"/>
    <rect x="81" y="10" width="358" height="203" fill="#1a1a1c"/>
    <rect x="0" y="226" width="520" height="14" rx="4" fill="#c9cacd"/>
    <rect x="0" y="238" width="520" height="5" rx="2" fill="#6d6e72"/>
    <circle cx="265" cy="111" r="22" fill="#0f6db5"/>
    <path d="M260 103 L272 111 L260 119 Z" fill="#fff"/>
  </svg>

  <h2 class="abs center h2" style="top:1277px">Warum sollte ich FLOWGRID ERP verwenden?</h2>
  <div class="abs center why-sub">
    <p>Lorem ipsum dolor sit amet, consetetur sadipscing elitr, sed diam nonumy eirmod tempor invidunt ut labore et dolore magna aliquyam erat, sed diam voluptua. At vero eos et accusam et justo duo dolores et ea rebum.</p>
    <p style="margin-top:18px">Stet clita kasd gubergren, no sea takimata sanctus est Lorem ipsum dolor sit amet. Lorem ipsum dolor sit amet, consetetur sadipscing elitr, sed diam nonumy eirmod tempor invidunt ut labore et dolore magna aliquyam erat,</p>
  </div>
  <a class="abs btn btn-anfrage">ANFRAGE</a>
  <a class="abs btn btn-support">SUPPORT</a>
</section>

<section>
  <div class="abs band"></div>
  <h2 class="abs center h2" style="top:1725px;color:#fff">Ihr Erfolg ist unser Erfolg</h2>
  <p class="abs center band-sub">Informieren Sie sich über die Lizenzierungs- und Kaufoptionen für die<br>Flowgrid ERP-Applikationen</p>

  <div class="abs feat-art" style="left:214px;top:1848px" role="img" aria-label="Isometrische Illustration eines Moduls"></div>
  <div class="abs feat-art" style="left:514px;top:1848px" role="img" aria-label="Isometrische Illustration einer Cloud-Plattform"></div>
  <div class="abs feat-art" style="left:814px;top:1848px" role="img" aria-label="Isometrische Illustration gestapelter Module"></div>

  <p class="abs feat-text" style="left:174px;top:2018px">Zahlen Sie nur für die ERP-Module, die Sie aktuell benötigen – Sie können bei einer Änderung Ihres Bedarfs zusätzliche Nutzer und weitere Funktionen hinzu.</p>
  <p class="abs feat-text" style="left:474px;top:2018px">FLOWGRID ERP ist auch im Abonnement über die Flowgrid Enterprise Cloud und als Managed-Cloud-Angebot von ausgesuchten Partnern erhältlich.</p>
  <p class="abs feat-text" style="left:774px;top:2018px">Für weitere Lizenzierungs- und Kaufoptionen wenden Sie sich bitte an Ihren FLOWGRID-Vertriebsbeauftragten.</p>

  <a class="abs center band-link">Informieren Sie sich ausführlich in unserer Broschüre &nbsp;→</a>
</section>

<section>
  <h2 class="abs center h2" style="top:2333px">Warum sollten Sie uns vertrauen?</h2>
  <p class="abs center trust-sub">Weil Sie es auch tun.</p>
  <div class="abs logos"><span>Halvorn</span><span>Tramo</span><span>Belvia</span><span>Stonemark</span><span>Netrion</span><span>Telvox</span></div>
  <svg class="abs chat" viewBox="0 0 54 54"><rect x="16" y="15" width="22" height="22" rx="5" fill="none" stroke="#fff" stroke-width="2.5"/><path d="M21 29 Q27 33 33 29" stroke="#fff" stroke-width="2" fill="none"/></svg>
</section>

<footer>
  <div class="abs footer"></div>
  <div class="abs footer-bar"></div>
  <div class="abs fcol" style="left:150px"><h4>ERP-Applikation</h4><ul><li>Übersicht</li><li>Cloud Plattform</li><li>Lorem Ipsum 1</li><li>Lorem Ipsum 2</li><li>Lorem Ipsum 3</li><li>Lorem Ipsum 4</li><li>Lorem Ipsum 5</li></ul></div>
  <div class="abs fcol" style="left:416px"><h4>Unternehmen</h4><ul><li>Über Flowgrid</li><li>Kunden</li><li>Kontakt</li></ul></div>
  <div class="abs fcol" style="left:681px"><h4>Karriere</h4><ul><li>Übersicht</li><li>Jobs <span class="hiring">Now hiring</span></li><li>Unsere Haltung</li><li>FAQ</li></ul></div>
  <div class="abs fcol bold" style="left:964px"><ul><li>Aktuelles</li><li>Lizenzmodelle</li><li>Sicherheit</li><li>Partner</li><li>Training</li></ul></div>

  <div class="abs fbrand"><span class="mark"></span>FLOWGRID</div>
  <div class="abs lang">German <svg width="10" height="6"><path d="M1 1 L5 5 L9 1" stroke="#fff" stroke-width="1.5" fill="none"/></svg></div>
  <div class="abs legal"><span>Impressum</span><span>Datenschutz</span><span>Sitemap</span><span>AGB</span></div>
  <div class="abs social"><span>Knotz</span><span>Circlo</span><span>Profila</span><span>Chirpa</span></div>
</footer>

</body>
</html>
```